Flyer für ambulanten Pflegedienst
Zielgruppe
Ambulanter Pflegedienst, Potentielle Kunden für Grund- und Behandlungspflege, nicht nur Pflegebedürftige, sondern auch Angehörige. Flyer dient zur Auslage, beispielsweise in Wartezimmern von Ärzten.
Aufgabenstellung
Ausführliches Briefing mit Aufbau und Text in der Anlage, ebenso das Bildmaterial, Fonts, Logos. Flyer in A4 Wickelfalz, bitte die Gestaltungsvorlage mit den Maßen des Druckanbieters (ebenfalls anbei) beachten. Vorerst hauptsächlich KI-generierte/Stockfotos vorhanden, Fotoshooting folgt im Juli und Bilder werden dann ggf. nochmal ersetzt um persönliche Ebene zu erzeugen. Der erste Wurf muss aber vorerst so erfolgen. Übergabe der Daten: Druckfähiges PDF, PDF mit Ebenen und AI

```html
<!DOCTYPE html>
<html lang="de">
<head>
<meta charset="utf-8">
<title>Flyer Hauskrankenpflege Lindner</title>
<link href="https://fonts.googleapis.com/css2?family=Quicksand:wght@400;500;600;700&display=swap" rel="stylesheet">
<style>
:root{
  --stage:#cfcfcf;
  --paper:#ffffff;
  --blue:#0e3c8f;
  --blue-deep:#0c3888;
  --blue-text:#123f95;
  --blue-line:#3f7fd6;
  --tint:#e8eef8;
  --grey:#7a7a7a;
  --light:#ffffff;
}
*{margin:0;padding:0;box-sizing:border-box}
html,body{width:960px;height:1200px;overflow:hidden}
body{background:var(--stage);font-family:'Quicksand',sans-serif;color:var(--blue-text);position:relative}
.spread{position:absolute;left:146px;width:668px;height:516px;box-shadow:0 6px 18px rgba(0,0,0,.18);overflow:hidden;background:var(--paper)}
.spread--outer{top:57px}
.spread--inner{top:627px}
.panel{position:absolute;top:0;height:516px;overflow:hidden}
.panel--white{background:linear-gradient(90deg,#fff 70%,#f1f1f3)}
.panel--blue{background:var(--blue);color:var(--light)}
.abs{position:absolute}
h2{font-weight:700;font-size:14px;line-height:17px}
p{font-size:8.7px;line-height:14.4px;font-weight:500;letter-spacing:-.05px}
.rule{position:absolute;height:1px;width:71px;background:var(--blue-text)}
.panel--blue .rule{background:var(--blue-line)}
.divider{position:absolute;height:1px;background:var(--blue-line)}
.checklist .item{position:absolute;left:17px;right:12px;padding-left:18px}
.check{position:absolute;left:0;top:2px;width:11px;height:11px}
.photo{position:absolute}
.brand{position:absolute;left:0;right:0;top:40px;text-align:center;font-weight:700;font-size:14px;color:var(--blue-text)}
.brand::before{content:"";display:inline-block;width:8px;height:8px;border-radius:50%;background:var(--blue-text);margin-right:6px;vertical-align:1px}
.cover-title{position:absolute;left:13px;top:278px;font-size:21.5px;line-height:26px;font-weight:700;color:var(--blue-text);white-space:nowrap}
.cover-sub{position:absolute;left:13px;top:379px;width:212px;font-size:12.2px;line-height:19px;font-weight:600;color:var(--blue-text)}
.bullets{position:absolute;left:13px;top:442px;list-style:none}
.bullets li{font-size:10.5px;line-height:16px;color:var(--grey);font-weight:400;padding-left:15px;position:relative}
.bullets li::before{content:"";position:absolute;left:0;top:6px;width:5px;height:5px;border-radius:50%;background:var(--blue-text)}
.quote-band{position:absolute;left:0;top:166px;width:226px;height:59px;background:var(--tint)}
.quote-band p{position:absolute;left:31px;top:13px;right:6px;font-weight:700;font-size:8.8px;line-height:14.4px}
</style>
</head>
<body>

<section class="spread spread--outer">

  <div class="panel panel--white" style="left:0;width:219px">
    <h2 class="abs" style="left:31px;top:29px">Pflege braucht Vertrauen.<br>Und Menschen, die da sind.</h2>
    <p class="abs" style="left:31px;top:79px;width:186px">Bei der Hauskrankenpflege Lindner arbeiten über 40 engagierte Mitarbeitende Hand in Hand – mit Herz, Respekt dan fachlicher Kompetenz.</p>
    <p class="abs" style="left:32px;top:190px;width:180px">Wir sind für Sie da.<br>Sie möchten sich informieren oder ein persönliches Gespräch vereinbaren? Wir beraten Sie gerne – unkompliziert, persönlich und unverbindlich.</p>
    <div class="rule" style="left:32px;top:305px"></div>
    <h2 class="abs" style="left:31px;top:353px">Kontakt</h2>
    <p class="abs" style="left:31px;top:387px;width:186px">Hauskrankenpflege Lindner<br>Am Weidenhof 12, 31299 Birkenau<br>Telefon: 0 5100-48 27 0<br>info@lindner-pflege.example<br>www.lindner-pflege.example<br>Bürozeiten: Mo., Di., Mi., Fr. 9 bis 12 Uhr und Do. 15 bis 17 Uhr</p>
  </div>

  <div class="panel panel--blue checklist" style="left:219px;width:221px">
    <h2 class="abs" style="left:17px;top:29px">Hilfe im Haushalt.<br>Entlastung im Alltag.</h2>
    <p class="abs" style="left:17px;top:79px;width:200px">Damit Sie sich zuhause weiterhin wohlfühlen können, bieten wir fachgerechte und zuverlässige Unterstützung:</p>

    <div class="item" style="top:147px">
      <svg class="check" viewBox="0 0 12 12" aria-hidden="true"><rect x=".7" y="1.5" width="9.5" height="9.5" rx="2" fill="none" stroke="#5fa0ff" stroke-width="1.1"/><path d="M3 6 L5.3 8.2 L11.3 1.2" fill="none" stroke="#5fa0ff" stroke-width="1.3"/></svg>
      <p>Hilfe im Haushalt: Von der Grundreinigung bis zur Wäschepflege.</p>
    </div>
    <div class="divider" style="left:17px;width:185px;top:183px"></div>
    <div class="item" style="top:190px">
      <svg class="check" viewBox="0 0 12 12" aria-hidden="true"><rect x=".7" y="1.5" width="9.5" height="9.5" rx="2" fill="none" stroke="#5fa0ff" stroke-width="1.1"/><path d="M3 6 L5.3 8.2 L11.3 1.2" fill="none" stroke="#5fa0ff" stroke-width="1.3"/></svg>
      <p>Alltagsbegleitung: Gesellschaft und Unterstützung, bila gewünscht.</p>
    </div>
    <div class="divider" style="left:17px;width:185px;top:225px"></div>
    <div class="item" style="top:233px">
      <svg class="check" viewBox="0 0 12 12" aria-hidden="true"><rect x=".7" y="1.5" width="9.5" height="9.5" rx="2" fill="none" stroke="#5fa0ff" stroke-width="1.1"/><path d="M3 6 L5.3 8.2 L11.3 1.2" fill="none" stroke="#5fa0ff" stroke-width="1.3"/></svg>
      <p>Betreuung: Strukturierte Hilfe nach individuellem Bedarf.</p>
    </div>

    <h2 class="abs" style="left:17px;top:375px">Kontakt</h2>
    <p class="abs" style="left:17px;top:416px;width:200px">So erreichen Sie uns:<br>Telefon: 0 5100-63 51 904<br>info@lindner-hausdienste.example<br>www.lindner-hausdienste.example<br>Bürozeiten: Mo., Di., Do., Fr. 8 bis 11 Uhr</p>
  </div>

  <div class="panel" style="left:440px;width:228px;background:#fff">
    <div class="photo" role="img" aria-label="Foto: Pflegekraft im Gespräch mit einer lächelnden älteren Dame zuhause, Zimmerpflanzen im Hintergrund" style="left:0;top:80px;width:228px;height:240px;background:linear-gradient(120deg,#e6e3dc 0%,#8fb0d4 35%,#d9c4a8 55%,#7fb0a5 80%,#e9ece6 100%)"></div>
    <div class="photo" aria-hidden="true" style="left:0;top:0;width:228px;height:110px;background:linear-gradient(180deg,#fff 55%,rgba(255,255,255,0))"></div>
    <div class="photo" aria-hidden="true" style="left:0;top:230px;width:228px;height:120px;background:linear-gradient(180deg,rgba(255,255,255,0),#fff 70%)"></div>
    <div class="brand">lindner hauskrankenpflege</div>
    <div class="cover-title">Weil das<br>eigene Zuhause<br>Lebensqualität ist.</div>
    <div class="cover-sub">Ihr ambulanter Plegedienst für die Region Birkenau und Weidenfeld.</div>
    <ul class="bullets">
      <li>24h erreichbar</li>
      <li>Persönliche Beratung</li>
      <li>MD-geprüfte Qualität</li>
    </ul>
  </div>
</section>

<section class="spread spread--inner">

  <div class="panel panel--white" style="left:0;width:226px">
    <h2 class="abs" style="left:31px;top:29px">Wer wir sind</h2>
    <p class="abs" style="left:31px;top:62px">Vertrauen beginnt mit Zuhören.</p>
    <p class="abs" style="left:31px;top:93px;width:194px">Pflege bedeutet für uns mehr als Versorgung. Deshalb nehmen wir uns Zeit für persönliche Gespräche und individuelle Lösungen, die zu Ihrem Leben passen.</p>
    <div class="quote-band"><p>”Unsere Pflege orientiert sich am Befinden der Menschen – nicht am Befund.”</p></div>
    <div class="photo" role="img" aria-label="Foto: Lächelnde Pflegerin in blauer Kleidung hält die Hand einer älteren Person" style="left:0;top:225px;width:226px;height:291px;background:linear-gradient(135deg,#c89a6a 0%,#e2c29c 35%,#2f5fb8 65%,#d9d2c6 100%)"></div>
  </div>

  <div class="panel panel--blue" style="left:226px;width:222px">
    <h2 class="abs" style="left:13px;top:29px">Unsere Leistungen</h2>
    <p class="abs" style="left:13px;top:61px">Unterstützung, die den Alltag leichter macht.</p>
    <div class="rule" style="left:13px;top:114px"></div>
    <p class="abs" style="left:13px;top:156px;width:202px">Grundpflege: Unterstützung bei Körperpflege, Mobilität und Ernährung.</p>
    <div class="divider" style="left:13px;width:196px;top:191px"></div>
    <p class="abs" style="left:13px;top:199px;width:202px">Behandlungspflege: Medizinische Versorgung nach ärztlicher Verordnung (z.B. Wundversorgung, Medikamentengabe).</p>
    <div class="divider" style="left:13px;width:196px;top:249px"></div>
    <p class="abs" style="left:13px;top:257px;width:202px">Betreuung &amp; Alltagsbegleitung: Stundenweise Betreuung, Unterstützung bei Demenz und Entlastung für Angehörige.</p>
    <div class="photo" role="img" aria-label="Foto: Lächelnde Haushaltshilfe in grünem Shirt mit Putzeimer und Reinigungsmitteln" style="left:13px;top:362px;width:196px;height:117px;background:linear-gradient(120deg,#cfe0e6 0%,#e8eef0 40%,#2f6b46 70%,#d8e4e8 100%)"></div>
  </div>

  <div class="panel panel--blue" style="left:448px;width:220px;background:var(--blue-deep)">
    <div class="photo" role="img" aria-label="Foto: Betreuerin in grünem Shirt und ältere Dame lachen gemeinsam auf einer Gartenbank" style="left:11px;top:110px;width:196px;height:116px;background:linear-gradient(135deg,#3f6a2a 0%,#6da33b 40%,#4c8a3a 60%,#cfc4c8 85%,#e8e4e6 100%)"></div>
    <p class="abs" style="left:11px;top:269px;width:202px">Verhinderungspflege: Auszeiten für pflegende Angehörige, um mal durchzuatmen.</p>
    <div class="divider" style="left:11px;width:196px;top:304px"></div>
    <p class="abs" style="left:11px;top:312px;width:202px">Beratung: Pflegeberatung nach § 37.3 SGB XI, Hilfe bei Anträgen und Fragen.</p>
    <div class="divider" style="left:11px;width:196px;top:351px"></div>
    <p class="abs" style="left:11px;top:355px;width:202px">Hausnotruf &amp; Palliative Versorgung: Sicherheit rund um die Uhr und spezialisierte Begleitung zum Ende des Lebens.</p>
  </div>
</section>

</body>
</html>
```